Harborline Washtek Laundry Service Company

I own a Coin Operated laundry business and need to include a picture of Coin operated machines.
Include:
Company Name: Harborline Washtek
For all your Coin Operated Laundry needs.Include: sales, service, and new installations with commissions as high as 50%
include 1187 N. Larkview Rd, Arcadia, Ca 90417
626-518-2790
Include: Contact: Dwight Menser

Target Market(s)

coin Laundry

Industry/Entity Type

Business

Requirements
Must have
• picture of machines
• Sales, Service, Installations

```html
<!DOCTYPE html>
<html lang="en">
<head>
<meta charset="utf-8">
<title>Harborline Washtek Laundry Service Company – Postcard</title>
<link rel="stylesheet" href="https://fonts.googleapis.com/css2?family=Oswald:wght@300;400&family=Roboto+Condensed:wght@400&family=Montserrat:wght@400;500&display=swap">
<style>
  :root {
    --panel-brown: #8c7565;
    --box-tan: #c2a698;
    --ink-dark: #1f1a17;
    --paper: #ffffff;
    --rule-grey: #b9b9b9;
    --frame-grey: #cfcfcf;
    --photo-pink: #e8756a;
    --photo-tan: #c9b08c;
    --photo-blue: #5f7fa6;
    --photo-ground: #e9eaee;
  }
  html, body {
    margin: 0;
    padding: 0;
    width: 1200px;
    height: 779px;
    overflow: hidden;
    background: var(--paper);
  }
  .postcard {
    position: relative;
    width: 1200px;
    height: 779px;
    background: var(--paper);
  }
  .front-panel {
    position: absolute;
    left: 10px;
    top: 10px;
    width: 594px;
    height: 759px;
    background: var(--panel-brown);
    overflow: hidden;
  }
  .company-name {
    position: absolute;
    left: 0;
    width: 100%;
    top: 58px;
    margin: 0;
    text-align: center;
    white-space: nowrap;
    color: var(--paper);
    font-family: "Oswald", sans-serif;
    font-weight: 300;
    font-size: 37px;
    line-height: 1;
    letter-spacing: -0.6px;
  }
  .tagline {
    position: absolute;
    left: 0;
    width: 100%;
    top: 130px;
    margin: 0;
    text-align: center;
    white-space: nowrap;
    color: var(--ink-dark);
    font-family: "Roboto Condensed", sans-serif;
    font-size: 25px;
    line-height: 1;
  }
  .services {
    position: absolute;
    left: 0;
    width: 100%;
    top: 165px;
    margin: 0;
    text-align: center;
    white-space: nowrap;
    color: var(--paper);
    font-family: "Roboto Condensed", sans-serif;
    font-size: 17px;
    line-height: 1;
  }
  .machines-photo {
    position: absolute;
    left: 0;
    top: 0;
    width: 594px;
    height: 759px;
  }
  .contact-box {
    position: absolute;
    left: 10px;
    top: 560px;
    width: 572px;
    height: 112px;
    box-sizing: border-box;
    background: var(--box-tan);
    border: 2px solid var(--ink-dark);
    text-align: center;
    font-family: "Montserrat", sans-serif;
    color: var(--ink-dark);
  }
  .contact-name {
    margin: 6px 0 0;
    font-size: 31px;
    font-weight: 500;
    line-height: 1.2;
  }
  .contact-phone {
    margin: 2px 0 0;
    font-size: 22px;
    letter-spacing: 1px;
    line-height: 1.2;
    display: flex;
    justify-content: center;
    align-items: center;
    gap: 8px;
  }
  .contact-address {
    margin: 3px 0 0;
    font-size: 16px;
    font-weight: 400;
    line-height: 1.2;
  }
  .phone-icon { width: 20px; height: 20px; }
  .mailing-side {
    position: absolute;
    left: 604px;
    top: 10px;
    width: 586px;
    height: 759px;
    box-sizing: border-box;
    border: 1px solid var(--frame-grey);
    border-left: none;
  }
  .stamp-box {
    position: absolute;
    left: 375px;
    top: 58px;
    width: 163px;
    height: 149px;
    border: 1px solid var(--rule-grey);
  }
  .address-line {
    position: absolute;
    left: 58px;
    width: 480px;
    height: 0;
    border-top: 1px solid var(--rule-grey);
  }
  .address-line.first { top: 305px; }
  .address-line.second { top: 391px; left: 62px; width: 476px; }
  .postal-box {
    position: absolute;
    left: 58px;
    top: 636px;
    width: 480px;
    height: 74px;
    border: 1px solid var(--rule-grey);
  }
</style>
</head>
<body>
<main class="postcard">
  <section class="front-panel">
    <h1 class="company-name">Harborline Washtek Laundry Service Company</h1>
    <p class="tagline">For all your Coin Operated Laundry needs.</p>
    <p class="services">Sales • Service • New Installations — commissions as high as 50%</p>

    <svg class="machines-photo" viewBox="0 0 594 759" role="img" aria-label="Photo of folded laundry: pink, tan and blue denim garments stacked on a light surface">
      <defs>
        <linearGradient id="laundry-tones" x1="0" y1="0" x2="1" y2="0">
          <stop offset="0" stop-color="var(--photo-pink)"/>
          <stop offset="0.36" stop-color="var(--photo-pink)"/>
          <stop offset="0.44" stop-color="var(--photo-tan)"/>
          <stop offset="0.52" stop-color="var(--photo-blue)"/>
          <stop offset="1" stop-color="var(--photo-blue)"/>
        </linearGradient>
      </defs>
      <polygon points="33,334 464,205 570,630 154,741" fill="var(--photo-ground)"/>
      <polygon points="95,305 455,205 525,500 112,528" fill="url(#laundry-tones)" opacity="0.92"/>
    </svg>

    <div class="contact-box">
      <p class="contact-name">Contact: Dwight Menser</p>
      <p class="contact-phone">
        <svg class="phone-icon" viewBox="0 0 24 24" aria-hidden="true">
          <path d="M6.6 2.5l3 3.2-1.9 2.6c1.2 2.6 3.4 4.9 6 6.1l2.6-1.9 3.2 3-1.8 3.3C11 18.4 5.6 13 3.3 4.3z" fill="var(--ink-dark)"/>
        </svg>
        626-518-2790
      </p>
      <p class="contact-address">1187 N. Larkview Rd, Arcadia, Ca 90417</p>
    </div>
  </section>

  <section class="mailing-side" aria-label="Mailing side">
    <div class="stamp-box"></div>
    <div class="address-line first"></div>
    <div class="address-line second"></div>
    <div class="postal-box"></div>
  </section>
</main>
</body>
</html>
```